Fatigued and Overloaded by COVID Messages? We need original illustrations to show that.

Everywhere you look there are messages about COVID. That is leading many people to feel fatigued and overloaded by the messages.

We surveyed U.S. adults March 20th - 24th, 2020 and measured message fatigue, information overload, perceived repetition, and perceived exaggeration. Here is how participants responded:

When it comes to coronavirus . . .
55% feel exhausted by all the messages.
54% feel overloaded by the amount of information.
51% feel that the messages are repetitive.
47% feel like messages exaggerate how bad it is.

In other words, almost half of U.S. adults show signs of message fatigue, information overload, perceived message repetition, and perceived message exaggeration.

We will continue to survey 400 adults every week for the next 16 weeks. Each time we will measure message fatigue, information overload, perceived repetition, and perceived exaggeration. We expect that it will increase over time.

What are we looking for? We need innovative and original illustrations that attempt to communicate these findings. The illustrations would visualize message fatigue, information overload, perceived message repetition, and perceived message exaggeration.

What sort of visual are we looking for? Our preference is for an original illustration (or set of illustrations). Our preference is for creative and powerful illustrations, but we are also open to the creative and well-executed infographics.

We need these images fast . We will award monetary prizes to the 3 best designs. If we like more than that, then we might purchase more (e.g., in past contests, we have purchased as many as 30 designs).

What we will need:
(1) The illustrations must be original and we will need the photoshop and/or illustrator files for all artwork. (By original, we mean that the illustrations are 100% created by you. Our organization requires that we utilize only original illustrated work. We have had issues with free imagery being pirated and reposted as free. We sidestep that issue by just having everything created.)

(2) The illustration should say, somewhere: "Based on a survey of 400 U.S. adults conducted March 20 - 24th, 2020."

(3) We will have almost 4 months worth of data by the time this is done. In other words, the illustrations might be able to help us present that weekly data.

(4) We have conducted other Artvendo projects. It might be helpful to examine designs we liked in the past. For example, here is another COVID project we just finished:

https://jobs.artvendo-example.com/job/5162048

Target Market(s)

U.S. adults

Requirements
Must have
• Original illustrations. Mobile friendly design. People will view this on their smartphones.
Nice to have
• A design that we can use to communicate the data across time.

```html
<!DOCTYPE html>
<html lang="en">
<head>
<meta charset="utf-8">
<title>The Weight of the Crown</title>
<link rel="stylesheet" href="https://fonts.googleapis.com/css2?family=Cinzel:wght@500;600&family=Alegreya+Sans:ital,wght@1,400;1,500;1,800&display=swap">
<style>
  :root{
    --teal:#6cc8c5;
    --ink:#2e6b6a;
    --sky:#ddf0f9;
    --mint:#c0e0da;
    --cream:#fdefd3;
    --orange:#f2915c;
    --peach-1:#fcd6a6;
    --peach-2:#fbb870;
    --peach-3:#f8a771;
    --peach-4:#f59566;
    --bubble:#fbb870;
    --white:#ffffff;
  }
  *{margin:0;padding:0;box-sizing:border-box}
  html,body{width:988px;height:1200px;overflow:hidden;background:var(--teal)}
  .poster{position:relative;width:988px;height:1200px;background:var(--teal);font-family:"Alegreya Sans",sans-serif;overflow:hidden}
  .decor{position:absolute;inset:0}
  .hero-art{position:absolute;left:18px;top:46px;width:322px;height:430px;border-radius:48% 52% 40% 60% / 45% 40% 60% 55%;
    background:radial-gradient(circle at 42% 32%, #f59566 0 38%, #fbd3a6 62%, rgba(108,200,197,0) 76%)}
  .title-small{position:absolute;left:393px;top:286px;font-family:"Cinzel",serif;font-weight:600;font-size:50px;letter-spacing:2px;color:var(--ink);line-height:1;white-space:nowrap}
  .title-big{position:absolute;left:268px;top:328px;font-family:"Cinzel",serif;font-weight:600;font-size:158px;letter-spacing:-4px;color:var(--ink);line-height:1;white-space:nowrap}
  .lede{position:absolute;left:195px;top:488px;width:540px;font-style:italic;font-weight:500;font-size:24.5px;line-height:35px;color:var(--ink)}
  .results{position:absolute;left:59px;top:628px;width:870px;height:520px;background:var(--white);border:2px solid var(--ink);border-radius:12px}
  .method{position:absolute;left:23px;top:16px;width:825px;height:160px;background:var(--cream);border-radius:12px;padding:8px 18px;color:var(--orange);font-style:italic;font-weight:500;font-size:25px;line-height:33px}
  .method p+p{margin-top:12px}
  .lead-in{position:absolute;left:43px;top:190px;font-style:italic;font-weight:500;font-size:25px;color:var(--ink)}
  .stat{position:absolute;top:235px;width:187px;height:262px;border-radius:12px}
  .stat--1{left:24px;background:var(--peach-1);color:var(--peach-4)}
  .stat--2{left:236px;background:var(--peach-2);color:#fff3e4}
  .stat--3{left:448px;background:var(--peach-3);color:#fde6d2}
  .stat--4{left:659px;background:var(--peach-4);color:#fde6d2}
  .battery{position:absolute;left:-10px;top:18px;width:100px;height:130px;overflow:visible}
  .stat-value{position:absolute;left:55px;top:10px;font-style:italic;font-weight:800;font-size:82px;line-height:1;letter-spacing:-3px;color:var(--ink)}
  .stat-value small{font-size:44px;letter-spacing:0}
  .stat-label{position:absolute;left:15px;top:150px;width:170px;font-style:italic;font-weight:400;font-size:24px;line-height:32.5px}
  .source{position:absolute;left:83px;top:1160px;font-style:italic;font-size:14.5px;color:#eefaf9}
</style>
</head>
<body>
<div class="poster">
  <svg class="decor" viewBox="0 0 988 1200" aria-hidden="true">
    <path d="M43 480 C60 420 150 440 230 360 C330 260 420 190 560 205 C650 215 700 250 690 330 C685 390 760 420 820 450 C900 500 870 560 880 628 L150 628 C80 600 30 540 43 480Z" fill="var(--sky)"/>
    <path d="M155 560 C170 470 240 420 290 400 C380 360 470 320 550 300 C640 280 720 320 770 380 C830 450 800 540 835 628 L190 628 C160 610 150 590 155 560Z" fill="var(--mint)"/>
    <path d="M665 95 C650 50 740 40 800 60 C860 80 920 110 915 170 C910 230 870 262 810 255 C760 250 730 230 700 200 C670 170 690 140 665 95Z" fill="var(--sky)"/>
    <path d="M655 70 C650 30 720 20 780 40 C840 60 900 80 900 140 C900 200 850 245 790 240 C740 236 710 210 700 170 C690 130 660 110 655 70Z" fill="var(--mint)"/>
    <g fill="none" stroke="var(--ink)" stroke-width="1" stroke-dasharray="6 5" opacity=".6">
      <path d="M800 155 C880 210 910 280 880 340 C850 400 720 420 620 380 C520 340 470 300 400 260 C360 235 330 190 400 160 C480 130 580 150 610 200 C630 240 620 300 590 380 C560 460 560 520 640 560 C720 590 820 580 870 540 C920 500 970 460 950 420"/>
      <path d="M160 540 C220 520 300 540 380 580 C420 600 400 620 360 628"/>
    </g>
    <g fill="var(--sky)">
      <path d="M706 55 l4 10 10 4 -10 4 -4 10 -4 -10 -10 -4 10 -4Z"/>
      <path d="M716 160 l3 7 7 3 -7 3 -3 7 -3 -7 -7 -3 7 -3Z"/>
      <path d="M479 176 l3 8 8 3 -8 3 -3 8 -3 -8 -8 -3 8 -3Z"/>
      <path d="M545 210 l3 7 7 3 -7 3 -3 7 -3 -7 -7 -3 7 -3Z"/>
      <path d="M944 324 l3 8 8 3 -8 3 -3 8 -3 -8 -8 -3 8 -3Z" fill="#eefaf9"/>
      <path d="M910 66 l2 5 5 2 -5 2 -2 5 -2 -5 -5 -2 5 -2Z" fill="#eefaf9"/>
    </g>
    <path d="M746 90 L826 123 L772 153Z" fill="#fff"/>
    <path d="M772 153 L790 140 L800 156Z" fill="#cfd8d6"/>
    <g>
      <path d="M620 200 a14 14 0 0 1 14 -14 h50 a22 22 0 0 1 0 50 h-64Z" fill="var(--bubble)"/>
      <text x="654" y="222" font-family="Alegreya Sans, sans-serif" font-weight="800" font-size="30" fill="#fde3c8" text-anchor="middle">@</text>
      <path d="M728 494 a14 14 0 0 1 14 -14 h44 a14 14 0 0 1 14 14 v12 h-50 a22 22 0 0 1 -22 -22Z" fill="var(--bubble)" transform="translate(0,-24)"/>
      <text x="763" y="496" font-family="Alegreya Sans, sans-serif" font-weight="800" font-size="34" fill="#fde3c8" text-anchor="middle">#</text>
      <path d="M97 528 a22 22 0 0 1 22 -25 h30 a20 20 0 0 1 20 20 v31 h-50 a22 22 0 0 1 -22 -26Z" fill="var(--bubble)"/>
      <g fill="none" stroke="#fde3c8" stroke-width="2.5">
        <circle cx="133" cy="529" r="17"/><ellipse cx="133" cy="529" rx="8" ry="17"/>
        <line x1="116" y1="523" x2="150" y2="523"/><line x1="116" y1="535" x2="150" y2="535"/>
      </g>
    </g>
    <g>
      <rect x="845" y="520" width="83" height="52" fill="var(--peach-3)"/>
      <rect x="855" y="498" width="64" height="50" fill="#fff"/>
      <g stroke="#d7dbdb" stroke-width="2"><line x1="860" y1="507" x2="905" y2="507"/><line x1="860" y1="514" x2="899" y2="514"/><line x1="860" y1="521" x2="890" y2="521"/><line x1="892" y1="535" x2="914" y2="535"/></g>
      <path d="M845 520 L886 550 L928 520 V572 H845Z" fill="var(--peach-2)"/>
    </g>
  </svg>

  <div class="hero-art" role="img" aria-label="Illustration of a kneeling figure carrying a giant coronavirus on its back"></div>

  <h1>
    <span class="title-small">THE WEIGHT OF THE</span>
    <span class="title-big">CROWN</span>
  </h1>

  <p class="lede">Almost half of U.S. adults show signs of message fatigue, information overload, perceived message repetition, and perceived message exaggeration.</p>

  <section class="results">
    <div class="method">
      <p>We surveyed U.S. adults from March 20th - 24th, 2020 and measured message fatigue, information overload, perceived repetition, and perceived exaggeration.</p>
      <p>Here is how participants responded:</p>
    </div>
    <p class="lead-in">When it comes to coronavirus . . .</p>

    <article class="stat stat--1">
      <svg class="battery" viewBox="0 0 100 130" aria-hidden="true">
        <rect x="20" y="2" width="22" height="10" rx="2" fill="var(--ink)"/>
        <rect x="4" y="10" width="56" height="108" rx="7" fill="#fff" stroke="var(--ink)" stroke-width="5"/>
        <rect x="9" y="57" width="46" height="56" fill="var(--peach-2)"/>
        <circle cx="64" cy="95" r="29" fill="#fff" stroke="var(--ink)" stroke-width="4"/>
      </svg>
      <p class="stat-value">55<small>%</small></p>
      <p class="stat-label">feel exhausted by all the messages.</p>
    </article>

    <article class="stat stat--2">
      <svg class="battery" viewBox="0 0 100 130" aria-hidden="true">
        <rect x="20" y="2" width="22" height="10" rx="2" fill="var(--ink)"/>
        <rect x="4" y="10" width="56" height="108" rx="7" fill="#fff" stroke="var(--ink)" stroke-width="5"/>
        <rect x="9" y="58" width="46" height="55" fill="var(--peach-2)"/>
        <circle cx="64" cy="95" r="29" fill="#fff" stroke="var(--ink)" stroke-width="4"/>
      </svg>
      <p class="stat-value">54<small>%</small></p>
      <p class="stat-label">feel overloaded by the amount of information.</p>
    </article>

    <article class="stat stat--3">
      <svg class="battery" viewBox="0 0 100 130" aria-hidden="true">
        <rect x="20" y="2" width="22" height="10" rx="2" fill="var(--ink)"/>
        <rect x="4" y="10" width="56" height="108" rx="7" fill="#fff" stroke="var(--ink)" stroke-width="5"/>
        <rect x="9" y="64" width="46" height="49" fill="var(--peach-4)"/>
        <circle cx="64" cy="95" r="29" fill="#fff" stroke="var(--ink)" stroke-width="4"/>
      </svg>
      <p class="stat-value">51<small>%</small></p>
      <p class="stat-label">feel that the messages are repetitive.</p>
    </article>

    <article class="stat stat--4">
      <svg class="battery" viewBox="0 0 100 130" aria-hidden="true">
        <rect x="20" y="2" width="22" height="10" rx="2" fill="var(--ink)"/>
        <rect x="4" y="10" width="56" height="108" rx="7" fill="#fff" stroke="var(--ink)" stroke-width="5"/>
        <rect x="9" y="67" width="46" height="46" fill="#f27f55"/>
        <circle cx="64" cy="95" r="29" fill="#fff" stroke="var(--ink)" stroke-width="4"/>
      </svg>
      <p class="stat-value">47<small>%</small></p>
      <p class="stat-label">feel like messages exaggerate how bad it is.</p>
    </article>
  </section>

  <p class="source">Based on a survey of 400 U.S. adults conducted March 20 - 24th, 2020.</p>
</div>
</body>
</html>
```